BOLD & MINIMALIST DESIGN NEEDED

We want a very bold but minimalistic business card design that is impactful and utilizes both sides of the business card. Our current logo is included for your use.

We want bold fonts and good use of negative space. We don't want the logo to overpower the design.

Target Market(s)

Professionals who are building new commercial buildings.

Industry/Entity Type

Construction

Contact Information for Business Card

Name, Title, email, office phone, cell phone, website

Font styles to use
Serif
Sans Serif

Requirements
Must have
• Bold design!

```html
<!DOCTYPE html>
<html lang="en">
<head>
<meta charset="utf-8">
<title>Ridgecrest Business Card</title>
<link rel="stylesheet" href="https://fonts.googleapis.com/css2?family=Arimo:wght@400;700&family=Crimson+Pro:wght@400&display=swap">
<style>
  :root {
    --page: #ffffff;
    --card-front: #fdfbf4;
    --card-back: #0d0e10;
    --ink: #1a1a2e;
    --ink-name: #222222;
    --accent: #7cc142;
    --white: #ffffff;
  }
  * { margin: 0; padding: 0; box-sizing: border-box; }
  html, body {
    width: 1200px; height: 544px; overflow: hidden;
    background: var(--page);
  }
  .canvas { position: relative; width: 1200px; height: 544px; }
  .card {
    position: absolute; top: 143px; width: 460px; height: 263px;
  }
  .card-front { left: 126px; background: var(--card-front); }
  .card-back { left: 604px; background: var(--card-back); }

  .person-icon { position: absolute; left: 29px; top: 53px; width: 20px; height: 22px; }
  .person-name {
    position: absolute; left: 56px; top: 46px;
    font-family: "Crimson Pro", Georgia, serif; font-weight: 400;
    font-size: 31px; line-height: 1; color: var(--ink-name);
  }
  .person-title {
    position: absolute; left: 56px; top: 84px;
    font-family: "Arimo", Arial, sans-serif; font-size: 12.5px; color: var(--ink);
  }
  .contact-list {
    position: absolute; left: 54px; top: 149px; list-style: none;
    font-family: "Arimo", Arial, sans-serif; font-size: 15px; color: var(--ink);
  }
  .contact-list li { height: 23.6px; line-height: 23.6px; }
  .contact-icon { position: absolute; left: 29px; width: 14px; height: 14px; }
  .icon-mail { top: 155px; }
  .icon-phone { top: 178px; }

  .brand {
    position: absolute; display: flex; align-items: center; gap: 8px;
    font-family: "Arimo", Arial, sans-serif; font-weight: 700;
    font-size: 30px; letter-spacing: 0.5px; line-height: 1;
  }
  .brand-mark { width: 14px; height: 14px; background: var(--accent); }
  .brand-front { left: 272px; top: 170px; color: var(--ink); }
  .brand-back { left: 50%; top: 50%; transform: translate(-50%, -50%); color: var(--white); }
</style>
</head>
<body>
<main class="canvas">
  <section class="card card-front">
    <svg class="person-icon" viewBox="0 0 20 22" aria-hidden="true">
      <circle cx="10" cy="5.5" r="5" fill="#1a1a2e"/>
      <path d="M0 17c0-4 4-5.5 10-5.5S20 13 20 17s-4 4.5-10 4.5S0 21 0 17z" fill="#1a1a2e"/>
    </svg>
    <h1 class="person-name">Morgan Ellery</h1>
    <p class="person-title">Director</p>

    <svg class="contact-icon icon-mail" viewBox="0 0 14 14" aria-hidden="true">
      <path d="M1 3h12v9H1z" fill="#1a1a2e"/>
      <path d="M2 4.5l5 3.5 5-3.5" fill="none" stroke="#fdfbf4" stroke-width="1.4"/>
    </svg>
    <svg class="contact-icon icon-phone" viewBox="0 0 14 14" aria-hidden="true">
      <path d="M2.5 1l2.5 0 1 3-1.6 1.2c.8 1.8 2.2 3.2 4 4L9.6 7.6l3 1v2.6c0 1-1 1.8-2 1.7C5.8 12.4 1.6 8.2 1 3.4 .9 2.2 1.5 1 2.5 1z" fill="#1a1a2e"/>
    </svg>
    <ul class="contact-list">
      <li>Email: morgan@ridgecrest.com</li>
      <li>Mobile: +1 555 014 2277</li>
      <li>Office: +1 555 019 3480</li>
      <li>www.ridgecrest.com</li>
    </ul>

    <div class="brand brand-front"><span class="brand-mark"></span>Ridgecrest</div>
  </section>

  <section class="card card-back">
    <div class="brand brand-back"><span class="brand-mark"></span>Ridgecrest</div>
  </section>
</main>
</body>
</html>
```